Tide 4 Tide letterhead design and business card design for electrical company

I need a letterhead that can be used for my invoices and quote books along with emails sent to clients. I have a logo and the logo of Guild tradespeople I just need all my information placed nicely with a good flow.

Business Name: Tide 4 Tide Electrical
Name: Darren Kolvetis
Abn: 57804219362
Licence Number: 39417
Number: 0400683541

Thank you in advanced

Target Market(s)

Electrical Clients

Industry/Entity Type

Business

Contact Information for Business Card

Name: Darren Kolvetis
Abn: 57804219362
Licence Number: 39417
Number: 0400683541

Font styles to use
Sans Serif

Colors

Designer to choose colors to be used in the design.

Requirements
Must have
• Must have my logo, guild tradespeople logo even if its smaller and in the corner and all details
Nice to have
• Domestic Commercial Industrial stated on there somewhere

```html
<!DOCTYPE html>
<html lang="en">
<head>
<meta charset="utf-8">
<title>Tide 4 Tide Electrical — Business Card</title>
<link rel="stylesheet" href="https://fonts.googleapis.com/css2?family=Open+Sans:wght@400;600;700&display=swap">
<style>
  :root {
    --backdrop: #3a3430;
    --card: #0d0d0e;
    --card-edge: #1c1c1e;
    --ink: #ffffff;
    --accent: #2f86d6;
    --silver: #c9c9cc;
    --rule: #1f3a5c;
  }
  * { box-sizing: border-box; margin: 0; padding: 0; }
  html, body {
    width: 1200px; height: 900px; overflow: hidden;
    background: var(--backdrop);
    font-family: "Open Sans", sans-serif;
  }
  .canvas {
    position: relative; width: 1200px; height: 900px;
    display: flex; align-items: center; justify-content: center; gap: 60px;
  }
  .card {
    position: relative; width: 520px; height: 300px;
    background: var(--card);
    border: 1px solid var(--card-edge);
    box-shadow: 0 18px 40px rgba(0,0,0,.45);
  }
  /* Front */
  .card-front { display: flex; }
  .brand-side {
    width: 48%; display: flex; flex-direction: column;
    justify-content: center; align-items: center; gap: 46px;
    padding-top: 20px;
  }
  .brand-name {
    color: var(--accent); font-weight: 700; font-size: 19px;
    letter-spacing: 1px; text-transform: uppercase; text-align: center; line-height: 1.25;
  }
  .guild-badge { display: flex; align-items: center; gap: 6px; }
  .guild-badge .mark { width: 28px; height: 28px; background: var(--ink); }
  .guild-badge .label {
    color: var(--ink); font-size: 11px; font-weight: 600; line-height: 1.05; text-transform: uppercase;
  }
  .divider { width: 1px; background: var(--rule); margin: 40px 0; }
  .details-side {
    flex: 1; padding: 44px 0 0 26px; color: var(--ink); font-size: 13px;
  }
  .person-name { font-size: 17px; font-weight: 600; text-transform: uppercase; margin-bottom: 10px; letter-spacing: .3px; }
  .id-line { line-height: 1.5; }
  .id-line .key { color: var(--accent); font-weight: 600; text-transform: uppercase; }
  .contact-list { list-style: none; margin-top: 8px; }
  .contact-list li { display: flex; align-items: center; gap: 8px; line-height: 1.45; }
  .contact-list svg { width: 10px; height: 10px; fill: var(--accent); flex: none; }
  .address { margin-top: 10px; line-height: 1.4; }
  /* Back */
  .card-back { display: flex; align-items: center; justify-content: center; }
  .back-name {
    color: var(--silver); font-weight: 700; font-size: 30px;
    letter-spacing: 2px; text-transform: uppercase; text-align: center; line-height: 1.2;
  }
</style>
</head>
<body>
<main class="canvas">
  <section class="card card-front">
    <div class="brand-side">
      <div class="brand-name">Tide 4 Tide<br>Electrical</div>
      <div class="guild-badge">
        <span class="mark"></span>
        <span class="label">Guild<br>Tradespeople<br>Member</span>
      </div>
    </div>
    <div class="divider"></div>
    <div class="details-side">
      <h1 class="person-name">Darren Kolvetis</h1>
      <p class="id-line"><span class="key">ABN:</span> 57804219362</p>
      <p class="id-line"><span class="key">Licence Number:</span> 39417</p>
      <ul class="contact-list">
        <li><svg viewBox="0 0 10 10"><path d="M2 0l2 2.5-1.2 1.2c.6 1.3 1.5 2.2 2.5 2.8L6.5 5.3 9 7.2 7.8 9.6C4 9 1 6 .4 2.2z"/></svg>0400683541</li>
        <li><svg viewBox="0 0 10 10"><path d="M0 2h10v6H0z"/></svg>info@youremail.com</li>
        <li><svg viewBox="0 0 10 10"><circle cx="5" cy="5" r="5"/></svg>www.websitename.com</li>
      </ul>
      <p class="address">1234, Address GoesHere,<br>Country name, 12345</p>
    </div>
  </section>
  <section class="card card-back">
    <div class="back-name">Tide 4 Tide<br>Electrical</div>
  </section>
</main>
</body>
</html>
```